Opening Specials Flyer for SmileHaven Dental

We require a flyer design for our promotions/special offers for our new opening of Dental Practice. Please make one page flyer with designs on front and back
Opening Specials must be eye catchy, with images
FRONT - OPENING SPECIALS
BACK - MAP and Introduce our NEW CLINIC
on Back - MUST SAY "FLIP BACK OF FLYER TO VIEW OPENING SPECIAL OFFERS"

Opening specials to our local residents of West Ryde

Colour Scheme: Green, grey, white
Celebrate the opening of our new clinic
Opening Specials for West Ryde Residents include:

1. NO GAP Checkup for the whole family
NO GAP - Checkup Clean Fluoride X-rays - (to eligible health fund members)
2. Dental Crowns at half price - Full Ceramic $900 (includes core and crown, root canal extra) (please use picture of ceramic crown attached) - must bring voucher/flyer
3. Power tooth Whitening (Corvel Glint)- $400 must bring voucher/flyer
1hr office in chair whitening, immediate whitening results
4. 20% off all General Dental Treatment (must bring flyer- please design this onto flyer)
5. Free Healthcover Dental for Kids (for those eligible under Junior Oral Care Program up to $1000) - please have healthcover logo
6. Free consultation for second opinion of treatment plans

Emergency dental care available after hours, please contact (02) 7395 2268

Offer valid until 31st May 2016
by appointment only
No Gap for eligible health fund members only
Address: Shop 7/51-53 Larkin Rd West Ryde 2114
Please have image of atlas view of this location

Behind the flyer (back) I would like to introduce our new clinic:
MUST INCLUDE - Flip behind for opening special offers!

SmileHaven Dental is your Local Family Dentist
Newly opened in March 2016, we aim to provide local residents with affordable dentistry with a gentle friendly approach. We are a child friendly practice and welcome you and your family to visit our new clinic.

www.smilehavenclinic.com.au
info@smilehavenclinic.com.au
(02) 7395 2268

Target Market(s)

Residents of West Ryde and Surrounding Suburbs
Children and Family

Industry/Entity Type

Dental Clinic

Colors
acd036
b2b2b2

Requirements
Must have
• (You may phrase as you please)
• Newly Opened Dental Clinic in West Ryde
• Special Offers until 31st May 2016
• Specials and clearly big font "NO GAP"
• Healthcover logo (colour) next to "Free Healthcover Dental for Kids
• MUST have SmileHaven Dental Logo
• Must inform that voucher must be brought in order to claim specials
• Must have address: Shop 7/51-53 Larkin Rd West Ryde 2114
• Must have Ph: (02) 7395 2268
Nice to have
• Image of dental crown - full ceramic (attached)
• Image of Corvel Glint Whitening
• Map of Shop 7/51-53 Larkin Rd West Ryde (Atlas View)
• Happy family picture

```html
<!DOCTYPE html>
<html lang="en">
<head>
<meta charset="utf-8">
<title>SmileHaven Dental – Opening Specials</title>
<link rel="stylesheet" href="https://fonts.googleapis.com/css2?family=Kaushan+Script&family=Oswald:wght@300;500;700&family=Lato:wght@400;700;900&display=swap">
<style>
:root{
  --green:#7bc41c;
  --green-text:#5ea611;
  --green-deep:#5a9e12;
  --grey:#6d6d6d;
  --grey-light:#b2b2b2;
  --ink:#3d3d3d;
  --white:#ffffff;
}
*{margin:0;padding:0;box-sizing:border-box}
html,body{width:907px;height:1200px;overflow:hidden;background:var(--white)}
.flyer{position:relative;width:907px;height:1200px;overflow:hidden;background:var(--white);font-family:"Lato",sans-serif;color:var(--ink)}
.layer{position:absolute;left:0;top:0}
.family-photo{z-index:1}
.top-swoosh{z-index:2}
.headline-box{position:absolute;z-index:4;left:39px;top:381px;width:436px;height:359px;background:var(--grey);border-radius:0 0 16px 16px;box-shadow:0 18px 16px -12px rgba(0,0,0,.35);text-align:center;padding-top:100px}
.headline-script{font-family:"Kaushan Script",cursive;color:var(--white);font-size:44px;line-height:1}
.headline-big{font-family:"Oswald",sans-serif;font-weight:700;color:var(--green);font-size:82px;line-height:1;margin-top:14px;letter-spacing:1px}
.headline-light{font-family:"Oswald",sans-serif;font-weight:300;color:var(--white);font-size:60px;line-height:1;margin-top:8px}
.patient-photo{position:absolute;z-index:1;left:0;top:770px;width:340px;height:250px;background:radial-gradient(ellipse at 45% 50%,#dcdcdc 0%,#ececec 45%,rgba(255,255,255,0) 75%)}
.brand{position:absolute;z-index:4;left:92px;top:888px;display:flex;align-items:center;gap:12px}
.brand-dot{width:26px;height:26px;border-radius:50%;background:var(--green)}
.brand-name{font-family:"Lato",sans-serif;font-weight:900;font-size:36px;color:var(--grey);line-height:1}
.specials{position:absolute;z-index:4;left:509px;top:440px;width:372px}
.specials-title{font-family:"Oswald",sans-serif;font-weight:700;color:var(--green-text);font-size:19px;line-height:1.12;text-transform:uppercase}
.offer-list{list-style:none;margin-top:14px}
.offer{display:flex;gap:12px;font-size:13.3px;line-height:1.3;margin-bottom:8px;color:#444}
.offer-num{font-family:"Lato",sans-serif;font-weight:900;font-style:italic;color:var(--green-text);font-size:20px;width:20px;flex:none;line-height:1.1}
.emergency{margin-top:14px;font-family:"Oswald",sans-serif;font-weight:500;color:var(--green-text)}
.emergency-line{font-size:19px;line-height:1.2}
.emergency-phone{font-size:28px;line-height:1.15}
.validity{margin-top:10px;font-size:14px;line-height:1.3;color:#333}
.validity-title{font-weight:700;font-size:22px;line-height:1.2}
.validity-note{color:var(--green-text)}
.bottom-swoosh{z-index:1;top:960px}
.contacts{position:absolute;z-index:4;left:150px;top:1090px;list-style:none;color:var(--white);font-size:18px}
.contact{display:flex;align-items:center;gap:14px;height:27px}
.contact svg{width:16px;height:16px;flex:none}
.contact-web{letter-spacing:1.5px}
</style>
</head>
<body>
<main class="flyer">
  <svg class="layer family-photo" width="907" height="440" viewBox="0 0 907 440" role="img" aria-label="Photo of a smiling family of four lying on the grass outdoors">
    <defs>
      <linearGradient id="photoTone" x1="0" y1="0" x2="1" y2="1">
        <stop offset="0" stop-color="#d9e8c2"/>
        <stop offset=".45" stop-color="#c9d4c8"/>
        <stop offset=".75" stop-color="#9fb6cc"/>
        <stop offset="1" stop-color="#c7dca6"/>
      </linearGradient>
    </defs>
    <path d="M0 0H907V240C700 340 400 380 0 345Z" fill="url(#photoTone)"/>
  </svg>

  <svg class="layer top-swoosh" width="907" height="440" viewBox="0 0 907 440" aria-hidden="true">
    <path d="M0 345C400 380 700 340 907 240V254C700 358 400 396 0 372Z" fill="#7bc41c"/>
    <path d="M0 384C400 404 700 368 907 268V325C700 405 400 418 0 410Z" fill="#6d6d6d"/>
  </svg>

  <section class="headline-box">
    <p class="headline-script">Celebrate the</p>
    <h1 class="headline-big">OPENING OF</h1>
    <p class="headline-light">OUR NEW CLINIC</p>
  </section>

  <div class="patient-photo" role="img" aria-label="Faded photo of a smiling senior woman"></div>

  <div class="brand">
    <span class="brand-dot"></span>
    <span class="brand-name">SmileHaven Dental</span>
  </div>

  <section class="specials">
    <h2 class="specials-title">Opening specials for West Ryde<br>residents include:</h2>
    <ol class="offer-list">
      <li class="offer"><span class="offer-num">1.</span><span>NO GAP Checkup for the whole family<br>NO GAP - Checkup Clean Fluoride X-rays - (to eligible health fund members)</span></li>
      <li class="offer"><span class="offer-num">2.</span><span>Dental Crowns at half price - Full Ceramic $900 (includes core and crown, root canal extra) (please use picture of ceramic crown attached) - must bring voucher/flyer</span></li>
      <li class="offer"><span class="offer-num">3.</span><span>Power tooth Whitening (Corvel Glint)- $400 must bring voucher/flyer 1hr office in chair whitening, immediate whitening results</span></li>
      <li class="offer"><span class="offer-num">4.</span><span>20% off all General Dental Treatment (must bring flyer- please design this onto flyer)</span></li>
      <li class="offer"><span class="offer-num">5.</span><span>Free Healthcover Dental for Kids (for those eligible under Junior Oral Care Program up to $1000) - please have healthcover logo</span></li>
      <li class="offer"><span class="offer-num">6.</span><span>Free consultation for second opinion of treatment plans</span></li>
    </ol>
    <div class="emergency">
      <p class="emergency-line">Emergency dental care available after hours,</p>
      <p class="emergency-phone">Please contact (02) 7395 2268</p>
    </div>
    <div class="validity">
      <p class="validity-title">Offer valid until 31st May 2016</p>
      <p>by appointment only</p>
      <p>No Gap for eligible health fund members only</p>
      <p class="validity-note">Address: Shop 7/51-53 Larkin Rd West Ryde 2114</p>
      <p class="validity-note">Please have image of atlas view of this location</p>
    </div>
  </section>

  <svg class="layer bottom-swoosh" width="907" height="240" viewBox="0 0 907 240" aria-hidden="true">
    <path d="M0 85C200 40 550 25 907 100V240H0Z" fill="#6d6d6d"/>
    <path d="M0 122C250 72 600 75 907 158V240H0Z" fill="#ffffff"/>
    <path d="M0 130C250 80 600 84 907 166V240H0Z" fill="#7bc41c"/>
    <path d="M430 240C600 175 780 165 907 190V240Z" fill="#5a9e12"/>
  </svg>

  <ul class="contacts">
    <li class="contact">
      <svg viewBox="0 0 16 16" aria-hidden="true"><path d="M3.5 1l2.5 3-1.5 2c1 2 2.5 3.5 4.5 4.5l2-1.5 3 2.5-1.5 2.5C7 15 1 9 1 2.5Z" fill="#fff"/></svg>
      <span>(02) 7395 2268</span>
    </li>
    <li class="contact">
      <svg viewBox="0 0 16 16" aria-hidden="true"><rect x="1" y="3" width="14" height="10" fill="#fff"/><path d="M1 3l7 6 7-6" fill="none" stroke="#7bc41c" stroke-width="1.4"/></svg>
      <span>info@smilehavenclinic.com.au</span>
    </li>
    <li class="contact">
      <svg viewBox="0 0 16 16" aria-hidden="true"><circle cx="8" cy="8" r="7" fill="#fff"/><path d="M1 8h14M8 1c-3 3.5-3 10.5 0 14M8 1c3 3.5 3 10.5 0 14" fill="none" stroke="#7bc41c" stroke-width="1"/></svg>
      <span class="contact-web">www.smilehavenclinic.com.au</span>
    </li>
  </ul>
</main>
</body>
</html>
```